BRIMLOW Pizza and Wraps

We need a website for a new restaurant called BRIMLOW "PIZZA AND WRAPS".
I have attached fonts, background images, logo, images, content etc.
can provide you with what you need to get the website design done fast and easy

I have uploaded more images of the venue and some menu items. let me know if there is anything I need to provide to make your mission clear and easy

Reason: i would like a little time to provide more feedback to designers

Industry/Entity Type

Restaurant

Coding

Coded - Design and coding required

Number of Pages Required

5+ page

Colors

Designer to choose colors to be used in the design.

Requirements
Must have
• PAGES:
• Our Story
• Menu
• Reservations
• Catering & Delivery
• Contact

```html
<!DOCTYPE html>
<html lang="en">
<head>
<meta charset="UTF-8">
<title>BRIMLOW Pizza and Wraps — Our Story</title>
<link href="https://fonts.googleapis.com/css2?family=Montserrat:wght@400;500;700&family=Sacramento&display=swap" rel="stylesheet">
<style>
  :root{
    --brick:#8a5a44;
    --wall-dark:#3b3631;
    --leaf:#4f6a3a;
    --panel-dark:rgba(20,18,16,.88);
    --brand-red:#ec1c24;
    --accent-yellow:#f5d315;
    --footer-bg:#050505;
    --white:#ffffff;
    --hummus:#e6cf8f;
    --bowl:#f4ede0;
  }
  *{box-sizing:border-box;margin:0;padding:0}
  html,body{width:1200px;height:632px;overflow:hidden}
  body{font-family:"Montserrat",Arial,sans-serif;color:var(--white);background:#000}
  .page{position:relative;width:1200px;height:632px;overflow:hidden}
  .venue-backdrop{position:absolute;inset:0 0 36px 0;
    background:
      radial-gradient(ellipse at 20% 85%, var(--leaf) 0%, transparent 45%),
      linear-gradient(90deg, var(--wall-dark) 0%, #5a4a3a 38%, var(--brick) 55%, #9a6550 80%, #7d5a45 100%);}
  .menu-toggle{position:absolute;left:37px;top:33px;width:24px;height:14px;
    display:flex;flex-direction:column;justify-content:space-between}
  .menu-toggle span{display:block;height:1px;background:var(--white)}
  .top-nav{position:absolute;left:102px;top:32px;font-size:10.5px;font-weight:500;letter-spacing:.1px}
  .top-nav a{color:var(--white);text-decoration:none}
  .social{position:absolute;left:102px;top:68px;display:flex;gap:8px}
  .social a{display:block;width:19px;height:19px;border-radius:50%;background:#1e1e1e;border:1px solid #555}
  .brand{position:absolute;right:38px;top:34px;font-size:40px;font-weight:700;color:var(--brand-red);letter-spacing:1px;line-height:1}
  .dish-photo{position:absolute;left:242px;top:124px;width:344px;height:344px;border-radius:50%;
    background:radial-gradient(circle, #d9b24a 0%, var(--hummus) 40%, #e9d9ae 70%, var(--bowl) 78%, var(--bowl) 100%);
    box-shadow:0 0 18px rgba(255,255,255,.35)}
  .story{position:absolute;left:614px;top:233px;width:376px;height:305px;background:var(--panel-dark);padding:10px 10px 0}
  .story h1{font-family:"Sacramento",cursive;font-weight:400;font-size:44px;color:var(--accent-yellow);text-align:center;line-height:1;height:54px;margin-top:4px}
  .story-body{background:var(--brand-red);padding:12px 9px 10px;font-size:10.6px;line-height:16.5px;text-align:justify;text-align-last:center;height:229px}
  .story-body p+p{margin-top:16.5px}
  .site-footer{position:absolute;left:0;bottom:0;width:1200px;height:36px;background:var(--footer-bg);border-top:1px solid var(--accent-yellow);
    font-size:10px;font-weight:500;color:var(--accent-yellow)}
  .site-footer .address{position:absolute;left:366px;top:11px}
  .site-footer .copyright{position:absolute;left:647px;top:11px}
</style>
</head>
<body>
<div class="page">
  <div class="venue-backdrop" role="img" aria-label="Restaurant storefront with brick wall, wooden door, glass windows and potted plants"></div>

  <div class="menu-toggle" aria-label="Open menu"><span></span><span></span><span></span></div>
  <nav class="top-nav"><a href="#">Make a Reservation</a> | <a href="#">Menu</a></nav>
  <div class="social"><a href="#" aria-label="Social page one"></a><a href="#" aria-label="Social page two"></a></div>

  <div class="brand">BRIMLOW</div>

  <div class="dish-photo" role="img" aria-label="Bowl of hummus topped with olive oil, chickpeas and paprika"></div>

  <section class="story">
    <h1>Our Story</h1>
    <div class="story-body">
      <p>Rich in heritage, <strong>Brimlow</strong> is a gathering place celebrating the Mediterranean's finest Produce.</p>
      <p><strong>Brimlow</strong> is the ultimate escape – the perfect spot to enjoy sensational food and drinks that showcases everything the Mediterranean has to offer in a single, sophisticated setting.</p>
      <p>Where an early morning walk to the bakery around the corner is a way of life, nothing beats the first batch of bread from the oven to start your day. So we combined a variety of best ingredients and delicacies for you to enjoy that experiencewhenever you got the urge to do so</p>
    </div>
  </section>

  <footer class="site-footer">
    <span class="address">Dummy Address | T: +92 300 5550147</span>
    <span class="copyright">Copyright @ 2017 hello@brimlowkitchen.com</span>
  </footer>
</div>
</body>
</html>
```